■依頼目的 / 概要
電子書籍Lumora本を出版いたしますので、
表紙デザイン作成をお願いいたします。

■納品物
下記での納品をお願い致します。

JPEG形式 及び PSD形式
横1600ピクセル x 縦2560ピクセル

■本の内容

<本のタイトル>
雑貨長者の資金調達術 〜開業ローン篇〜

<サブタイトル>
会社をつくる お金を借りる 原資ができる

<キャッチコピー>
貯金してから起業なんて絶対ダメ!

<著者名>
早川蒼一

■デザイン要望
・本のタイトル / キャッチコピー / 著者名の反映をお願いします

デザインイメージ

・人物や風景の画像を背景にしていただき、
その上にタイトル等コピーを記載

・シンプルな背景にタイトル等のコピーを記載

・資産形成に関する指南書。
その第一歩である新規創業融資に
焦点を当てた内容になっていますが、
お金に関することだけではなく、
人間関係や人生設計にまで
踏み込んだ内容になっています。

・楽して稼ぐといったレベルの低いイメージをもたせるような
デザインにはしたくありません。

<表現したいイメージなど>
・高級感
・かっこいい
・信頼感

<表現したくないイメージ>
・安っぽい
・嘘くさい
・大衆的

<利用画像について>
画像素材を使用される場合には、
商用利用可の素材をお願いします。

■その他
デザインを考えるのに必要な情報が他にございましたら、
お答えしますので、遠慮なくご連絡ください。

数あるご提案の中で、もっとも世界観を表現していただいているものを当選に選ばせていただきました。

この度は、たくさんのご提案ありがとうございました。
レベルの高いご提案が多く、非常に良いデザインを得ることができました。
今回、ご縁がなかったデザイナー様。また次回、ご提案いただければ幸いです。
ありがとうございました!

```html
<!DOCTYPE html>
<html lang="ja">
<head>
<meta charset="utf-8">
<title>雑貨長者の資金調達術 開業ローン篇</title>
<link href="https://fonts.googleapis.com/css2?family=Noto+Sans+JP:wght@700;900&family=Noto+Serif+JP:wght@600;700&display=swap" rel="stylesheet">
<style>
  :root {
    --sky-top: #e9eef3;
    --sky-mid: #8c98a6;
    --floor: #2d3540;
    --ink-dark: #1a1d22;
    --band-top: #5e2553;
    --band-bottom: #3a1233;
    --white: #ffffff;
    --title-shadow: #0c0f14;
    --cross: #e0262b;
    --arrow: #e8a7d6;
    --money: #b8c39a;
  }
  html, body { margin: 0; padding: 0; overflow: hidden; }
  body { width: 764px; height: 1200px; background: var(--ink-dark); }
  h1, p { margin: 0; }
  .cover {
    position: relative; width: 764px; height: 1200px; overflow: hidden;
    font-family: "Noto Sans JP", sans-serif; color: var(--white);
  }
  .cover__photo {
    position: absolute; left: 0; top: 0; width: 764px; height: 782px;
    background: linear-gradient(180deg, var(--sky-top) 0%, #c6cfd8 22%, var(--sky-mid) 48%, #4a5563 70%, var(--floor) 100%);
  }
  .cover__band {
    position: absolute; left: 0; top: 780px; width: 764px; height: 420px;
    background: radial-gradient(ellipse at 50% 40%, #6f2d63 0%, var(--band-top) 45%, var(--band-bottom) 100%);
  }
  .title {
    position: absolute; left: 0; width: 764px; text-align: center;
    font-weight: 900; letter-spacing: 2px;
    text-shadow: 0 0 6px var(--title-shadow), 0 0 14px var(--title-shadow), 3px 3px 0 var(--title-shadow);
  }
  .title__lead { top: 462px; font-size: 52px; line-height: 1; }
  .title__main { top: 530px; font-size: 88px; line-height: 1; }
  .title__series {
    position: absolute; left: 0; width: 764px; top: 652px; text-align: center;
    font-size: 30px; font-weight: 700; letter-spacing: 3px; line-height: 1;
    text-shadow: 0 0 6px var(--title-shadow), 0 0 10px var(--title-shadow);
  }
  .catch {
    position: absolute; left: 0; width: 764px; top: 788px; text-align: center;
    font-family: "Noto Serif JP", serif; font-weight: 700; font-size: 30px; line-height: 1.6;
  }
  .catch ruby rt { font-size: 13px; color: var(--cross); }
  .catch__cross { color: var(--cross); font-family: "Noto Sans JP", sans-serif; font-weight: 900; }
  .steps {
    position: absolute; left: 0; width: 764px; top: 852px; text-align: center; line-height: 1.3;
    font-family: "Noto Serif JP", serif; font-weight: 700; font-size: 32px; white-space: nowrap;
  }
  .steps__arrow { display: inline-block; vertical-align: middle; margin: 0 6px; }
  .money {
    position: absolute; left: 302px; top: 935px; width: 160px; height: 66px; border-radius: 4px;
    background: linear-gradient(180deg, #d7dec0, var(--money) 60%, #8e9a70);
  }
  .author {
    position: absolute; left: 0; width: 764px; top: 1020px; text-align: center; line-height: 1.3;
    font-family: "Noto Serif JP", serif; font-weight: 600; font-size: 40px; letter-spacing: 8px;
  }
</style>
</head>
<body>
  <div class="cover">
    <div class="cover__photo" role="img" aria-label="オフィスの窓際に並ぶビジネスパーソンのシルエットと床への映り込み"></div>
    <div class="cover__band"></div>

    <h1 class="title title__lead">雑貨長者の</h1>
    <p class="title title__main">資金調達術</p>
    <p class="title__series">開業ローン篇</p>

    <p class="catch">貯金してから起業なんて<ruby>絶対<rt>ダメ</rt></ruby><span class="catch__cross">✕</span>!</p>

    <p class="steps">会社をつくる<svg class="steps__arrow" width="30" height="22" viewBox="0 0 30 22"><path d="M0 7h16V0l14 11-14 11v-7H0z" fill="var(--arrow)"/></svg>お金を借りる<svg class="steps__arrow" width="30" height="22" viewBox="0 0 30 22"><path d="M0 7h16V0l14 11-14 11v-7H0z" fill="var(--arrow)"/></svg>原資ができる</p>

    <div class="money" role="img" aria-label="積み重なった紙幣の束"></div>

    <p class="author">早川蒼一</p>
  </div>
</body>
</html>
```